Shoes & Inserts Postcard Campaign

Hi,
We are looking to send a postcard to our patients reminding them that they may be eligible for shoes and inserts in the new calendar year. The patient demographic is mostly 50 and above.

We plan on uploading the image to Brimo Cards and have them create the postcard for us to be sent out.
Dimensions: 4.2"x5.5"
Front & Back Design
Images should be in high resolution. Entire postcard to be high resolution, if not vector.
I've attached a sample of what we used to have with the dimension parameters and our logo.

Verbiage can be the same, switch it to 2023. Front of the postcard doesn't need our logo. Looking for eye catching. Warm and welcoming.

Thank you,
Darren Osk

```html
<!DOCTYPE html>
<html lang="en">
<head>
<meta charset="utf-8">
<title>Shoes &amp; Inserts Postcard</title>
<link href="https://fonts.googleapis.com/css2?family=Fira+Sans+Condensed:wght@600;700&family=Fira+Sans:wght@500;600&family=Noto+Serif&display=swap" rel="stylesheet">
<style>
  :root {
    --stage: #8f8f8f;
    --orange: #f0884f;
    --teal: #6ac8b0;
    --teal-ring: #a7cdbb;
    --peach-ring: #f1c3a8;
    --button: #2fdca5;
    --mail-area: #e0e0e0;
    --white: #ffffff;
    --ink: #111111;
    --alert: #ff0000;
  }
  * { box-sizing: border-box; margin: 0; padding: 0; }
  html, body { width: 1049px; height: 1200px; overflow: hidden; }
  body { background: var(--stage); position: relative; font-family: "Fira Sans", sans-serif; }

  .postcard { position: absolute; left: 236px; width: 577px; height: 440px; overflow: hidden; box-shadow: 0 1px 3px rgba(0,0,0,.35); }
  .postcard--front { top: 131px; }
  .postcard--back { top: 629px; }
  .postcard svg.art { position: absolute; inset: 0; width: 577px; height: 440px; }

  /* front */
  .headline { position: absolute; left: 29px; top: 24px; font-family: "Fira Sans Condensed", sans-serif; font-weight: 700; font-size: 34px; line-height: 31px; color: var(--white); letter-spacing: .3px; }
  .front-contact { position: absolute; right: 25px; top: 366px; text-align: right; color: var(--white); font-family: "Fira Sans Condensed", sans-serif; font-weight: 700; }
  .front-contact .phone { font-size: 38px; line-height: 36px; }
  .front-contact .web { font-size: 20px; line-height: 22px; }

  /* back */
  .tagline { position: absolute; left: 26px; top: 22px; font-family: "Fira Sans Condensed", sans-serif; font-weight: 700; color: var(--orange); }
  .tagline .line-1 { display: block; font-size: 48px; line-height: 42px; }
  .tagline .line-2 { display: block; font-size: 35px; line-height: 34px; }
  .intro { position: absolute; left: 32px; top: 102px; width: 230px; font-size: 14.5px; line-height: 17px; font-weight: 500; color: var(--ink); }
  .intro .new { color: var(--alert); }

  .practice { position: absolute; right: 149px; top: 32px; text-align: right; }
  .practice-name { display: flex; align-items: center; justify-content: flex-end; gap: 8px; font-family: "Fira Sans Condensed", sans-serif; font-weight: 700; font-size: 17px; line-height: 17px; color: var(--orange); }
  .practice-name .mark { width: 34px; height: 34px; border-radius: 50%; background: var(--teal); flex: none; }
  .practice-address { margin-top: 9px; font-family: "Noto Serif", serif; font-size: 12px; line-height: 16px; color: var(--ink); }

  .call-panel { position: absolute; left: 0; top: 204px; width: 292px; text-align: center; color: var(--white); }
  .call-panel .ask { font-size: 14px; line-height: 18px; font-weight: 600; }
  .call-panel .away { margin-top: 5px; font-family: "Noto Serif", serif; font-size: 13px; line-height: 16px; }
  .call-panel .phone { font-size: 28px; line-height: 30px; font-weight: 600; letter-spacing: 1px; }
  .call-panel .request { display: inline-block; margin-top: 4px; width: 165px; height: 21px; border-radius: 5px; background: var(--button); color: var(--ink); font-family: "Noto Serif", serif; font-size: 12px; line-height: 21px; }
  .call-panel .fine-print { margin-top: 8px; font-size: 9px; line-height: 12px; font-weight: 500; }
</style>
</head>
<body>

<section class="postcard postcard--front">
  <svg class="art" viewBox="0 0 825 630" aria-hidden="false">
    <defs>
      <linearGradient id="scene" x1="0" y1="0" x2="0" y2="1">
        <stop offset="0" stop-color="#a7c75a"/>
        <stop offset=".45" stop-color="#9aa56a"/>
        <stop offset=".7" stop-color="#9b6a70"/>
        <stop offset="1" stop-color="#a5475e"/>
      </linearGradient>
      <linearGradient id="insole-photo" x1="0" y1="0" x2="1" y2="1">
        <stop offset="0" stop-color="#d9d9d6"/>
        <stop offset=".5" stop-color="#c9c6b4"/>
        <stop offset="1" stop-color="#6f7470"/>
      </linearGradient>
      <linearGradient id="arch-photo" x1="0" y1="0" x2="0" y2="1">
        <stop offset="0" stop-color="#c9a590"/>
        <stop offset="1" stop-color="#f2efea"/>
      </linearGradient>
    </defs>
    <rect class="scene-photo" width="825" height="630" fill="url(#scene)" role="img" aria-label="Photo of a walker's legs in coral running shoes on a park path"/>
    <circle class="orange-disc" cx="170" cy="80" r="300" fill="var(--orange)" opacity=".95"/>
    <circle cx="197" cy="431" r="182" fill="#f4ddd2" opacity=".8"/>
    <circle cx="197" cy="431" r="172" fill="var(--teal-ring)"/>
    <circle cx="197" cy="431" r="162" fill="url(#insole-photo)" role="img" aria-label="Photo of hands fitting a yellow insert into a black sneaker"/>
    <circle cx="350" cy="323" r="98" fill="#f6dccd" opacity=".75"/>
    <circle cx="350" cy="323" r="90" fill="var(--peach-ring)"/>
    <circle cx="350" cy="323" r="80" fill="url(#arch-photo)" role="img" aria-label="Photo of a custom arch insert held under a foot"/>
  </svg>
  <h1 class="headline">HAVE YOU<br>ORDERED THIS<br>YEAR'S SHOES<br>&amp; INSERTS?</h1>
  <div class="front-contact">
    <div class="phone">877-555-0148</div>
    <div class="web">WWW.STRIDEWELLFEET.COM</div>
  </div>
</section>

<section class="postcard postcard--back">
  <svg class="art" viewBox="0 0 825 630" aria-hidden="true">
    <defs>
      <clipPath id="panel-clip"><rect x="0" y="0" width="417" height="525"/></clipPath>
    </defs>
    <rect class="mail-area" width="825" height="630" fill="var(--mail-area)"/>
    <rect class="message-area" x="0" y="0" width="417" height="525" fill="var(--white)"/>
    <rect class="return-area" x="0" y="0" width="643" height="196" fill="var(--white)"/>
    <circle clip-path="url(#panel-clip)" cx="200" cy="494" r="260" fill="var(--teal)"/>
    <rect class="teal-strip" x="0" y="500" width="100" height="130" fill="var(--teal)"/>
  </svg>

  <h2 class="tagline"><span class="line-1">WE KEEP</span><span class="line-2">YOU MOVING</span></h2>
  <p class="intro">We are pleased to inform that you may be eligible for a <span class="new">NEW</span> pair of shoes &amp; inserts!</p>

  <div class="practice">
    <div class="practice-name"><span class="mark"></span><span>HILLCREST<br>FOOT &amp; ANKLE</span></div>
    <p class="practice-address">220 Maple Grove Rd<br>Ste. 140, Hillcrest, MD 21700</p>
  </div>

  <div class="call-panel">
    <p class="ask">Please call our office to<br>schedule your appointment.</p>
    <p class="away">We Are A Phone Call Away</p>
    <p class="phone">(877)555-0148</p>
    <span class="request">Request An Appointment</span>
    <p class="fine-print">*Last day to place a shoe order is 10/31/23.*<br>**If you have received your shoes and<br>inserts for 2023, please disregard.**</p>
  </div>
</section>

</body>
</html>
```